New Business Card Design Project

Target Market(s)

Passing cards out

Industry/Entity Type

Asphalt contractor

Contact Information for Business Card

Crestwick Paving

Colors
FFC000
F8CF3A
FAE287
FDF2CF
FEFAEE
F0912C
F2A743
F7CA91
FBE8D2
FDF5EE
EE7325
F08F49
F5BC92
FAE3D3
FDF4ED

Requirements
Must have
• Asphalt
Nice to have
• Would like to have 2 pictures on it of equipment

```html
<!DOCTYPE html>
<html lang="en">
<head>
<meta charset="utf-8">
<title>Crestwick Paving – Business Card</title>
<link rel="stylesheet" href="https://fonts.googleapis.com/css2?family=Audiowide&family=Open+Sans:wght@500&display=swap">
<style>
  :root {
    --page-bg: #3a3a3a;
    --card-black: #1b1b1b;
    --accent-orange: #f0912c;
    --accent-gold: #ffc000;
    --text-white: #ffffff;
    --asphalt-dark: #4a4a4a;
    --asphalt-light: #8a8a88;
    --sky: #a9c4dc;
  }
  html, body {
    margin: 0;
    width: 1200px;
    height: 1186px;
    overflow: hidden;
    background: var(--page-bg);
  }
  .business-card {
    position: absolute;
    left: 100px;
    top: 307px;
    width: 1000px;
    height: 571px;
    border-radius: 28px;
    overflow: hidden;
    background: var(--card-black);
    box-shadow: 0 12px 30px rgba(0,0,0,0.45);
  }
  .card-shapes {
    position: absolute;
    inset: 0;
    width: 1000px;
    height: 571px;
  }
  .brand-mark {
    position: absolute;
    left: 70px;
    top: 110px;
    width: 300px;
    display: flex;
    align-items: center;
    gap: 16px;
  }
  .brand-dot {
    flex: none;
    width: 30px;
    height: 30px;
    border-radius: 50%;
    background: var(--accent-orange);
  }
  .brand-name {
    font-family: "Audiowide", sans-serif;
    font-size: 38px;
    line-height: 1.1;
    color: var(--text-white);
    letter-spacing: 1px;
  }
  .person-name {
    position: absolute;
    margin: 0;
    font-family: "Audiowide", sans-serif;
    font-size: 34px;
    color: var(--text-white);
    letter-spacing: 1px;
    line-height: 55px;
  }
  .person-name--primary { left: 40px; top: 330px; }
  .person-name--secondary { left: 560px; top: 270px; }
  .contact-list {
    position: absolute;
    left: 40px;
    top: 420px;
    margin: 0;
    padding: 0;
    list-style: none;
    font-family: "Open Sans", sans-serif;
    font-weight: 500;
    font-size: 24px;
    color: var(--text-white);
  }
  .contact-item {
    display: flex;
    align-items: center;
    gap: 14px;
    height: 38px;
  }
  .contact-icon {
    width: 24px;
    height: 24px;
    flex: none;
  }
</style>
</head>
<body>
  <article class="business-card">
    <svg class="card-shapes" viewBox="0 0 1000 571" aria-hidden="false">
      <defs>
        <linearGradient id="equipmentPhotoTone" x1="0" y1="0" x2="0" y2="1">
          <stop offset="0" stop-color="var(--sky)"/>
          <stop offset="0.45" stop-color="#d9a441"/>
          <stop offset="1" stop-color="#6d6a64"/>
        </linearGradient>
        <linearGradient id="asphaltTone" x1="0" y1="0" x2="1" y2="1">
          <stop offset="0" stop-color="var(--asphalt-light)"/>
          <stop offset="1" stop-color="var(--asphalt-dark)"/>
        </linearGradient>
      </defs>
      <polygon points="380,0 1000,0 1000,270 484,270" fill="url(#equipmentPhotoTone)" role="img" aria-label="Photo of orange asphalt dump trucks parked in a yard"/>
      <polygon points="505,325 1000,325 1000,571 600,571" fill="url(#asphaltTone)" role="img" aria-label="Photo of asphalt pavement texture"/>
      <polygon class="name-band" points="484,270 1000,270 1000,325 505,325" fill="var(--accent-orange)"/>
      <polygon class="name-band" points="0,330 507,330 528,385 0,385" fill="var(--accent-orange)"/>
    </svg>

    <div class="brand-mark">
      <span class="brand-dot"></span>
      <span class="brand-name">CRESTWICK<br>PAVING</span>
    </div>

    <p class="person-name person-name--primary">DALE HARMON</p>
    <p class="person-name person-name--secondary">WADE HARMON</p>

    <ul class="contact-list">
      <li class="contact-item">
        <svg class="contact-icon" viewBox="0 0 24 24"><rect width="24" height="24" rx="5" fill="var(--accent-orange)"/><path d="M8 6c-1 0-2 1-2 2 0 5 5 10 10 10 1 0 2-1 2-2l-3-2-1.5 1.5c-2-1-3-2-4-4L11 10 9 6z" fill="var(--text-white)"/></svg>
        <span>555 214-7730</span>
      </li>
      <li class="contact-item">
        <svg class="contact-icon" viewBox="0 0 24 24"><rect width="24" height="24" rx="5" fill="var(--accent-orange)"/><rect x="5" y="7" width="14" height="10" rx="1" fill="var(--text-white)"/><path d="M5 8l7 5 7-5" fill="none" stroke="var(--accent-orange)" stroke-width="1.5"/></svg>
        <span>crestwickpaving@mail.com</span>
      </li>
    </ul>
  </article>
</body>
</html>
```